Australian Real Estate Sales Consultant needs web design please.

I am a female residential real estate sales consultant for a large australian real estate franchise.
I need a web design for "wordpress" that contains an area that will accommodate my photo and details and company logo.
A large area that contains a feature property where images are on something like a slide show.
Tabs or something similar with images for Selling, Sold, Photography and News where people can look at listings but I do not want people to be able to post a comment.
Reason: Need more designers, may be forced to change to wordpress and offer more money.
Reason: Sorry for the delay, I have been concentrating on another project which I needed completed. I am now able to focus on my web design project and hope to have it all set up in the next 10 days as it is a high priority for me. Thank you for your patience and I will begin providing feedback to your designs shortly. Thanks, Marisska.
Target Market(s)
Potential sellers or purchasers of residential property
Industry/Entity Type
Residential
Requirements
Must have
- Ease of changing property photos and info
Nice to have
- Bright attractive colours

```html
<!DOCTYPE html>
<html lang="en">
<head>
<meta charset="utf-8">
<title>Harbourline – Marisska Hartwell</title>
<link href="https://fonts.googleapis.com/css2?family=PT+Sans:wght@400;700&display=swap" rel="stylesheet">
<style>
:root{
  --red:#d21a1a;
  --ink:#333;
  --text:#555;
  --muted:#a5a5a5;
  --rule:#d9d9d9;
  --footer:#3a3a3a;
  --blue:#1a5fa8;
}
*{box-sizing:border-box;margin:0;padding:0}
html,body{width:1098px;height:1200px;overflow:hidden}
body{position:relative;font-family:"PT Sans",sans-serif;font-size:11px;color:var(--text);background:linear-gradient(#f3f7fa 0,#fff 60px) 0 395px/100% 100% no-repeat,#fff}
.abs{position:absolute}
.site-header{position:absolute;left:0;top:0;width:1098px;height:90px;background:linear-gradient(#f4f4f4,#fff)}
.brand{position:absolute;left:126px;top:27px;height:38px;display:flex;align-items:center;gap:8px;font-size:24px;font-weight:700;color:var(--red)}
.brand-mark{width:22px;height:22px;background:var(--blue)}
.main-nav{position:absolute;top:46px;left:0;font-size:11.5px;color:var(--ink);text-transform:uppercase}
.main-nav a{position:absolute;white-space:nowrap;color:inherit;text-decoration:none}
.main-nav a.active{color:var(--red)}
.hero{position:absolute;left:0;top:90px;width:1098px;height:305px;background:linear-gradient(90deg,#b89c80 0,#9a8268 40%,#8c7058 70%,#a0846a 100%)}
.hero-panel{position:absolute;left:106px;top:86px;width:462px;height:204px;background:rgba(95,85,75,.78);color:#fff;padding:24px 0 0 23px}
.hero-panel h1{font-weight:400;font-size:31px;letter-spacing:-.5px;line-height:40px}
.hero-panel p{width:410px;font-size:11px;line-height:14.5px;margin-top:3px}
.btn-readmore{position:absolute;left:23px;top:127px;width:97px;height:25px;border-radius:3px;background:linear-gradient(#e8302a,#c11414);color:#fff;font-weight:700;font-size:12px;line-height:25px;padding-left:13px;box-shadow:0 1px 2px rgba(0,0,0,.4)}
.btn-readmore:after{content:"";position:absolute;right:13px;top:9px;border:4px solid transparent;border-left:5px solid #fff;border-right:0}
.dots{position:absolute;left:363px;top:174px;display:flex;gap:8px}
.dots i{width:11px;height:11px;border-radius:50%;border:1.5px solid #fff;display:block}
.dots i.on{background:#fff}
.section-title{position:absolute;font-size:17px;color:var(--ink);font-weight:400}
.rule{position:absolute;height:1px;background:var(--rule)}
.listing-frame{position:absolute;width:257px;height:183px;background:#fff;box-shadow:0 0 4px rgba(0,0,0,.25);padding:6px}
.listing-photo{width:100%;height:100%}
.ribbon{position:absolute;right:-4px;top:-4px}
.listing-type{position:absolute;font-weight:700;font-size:12px;color:var(--ink)}
.listing-desc{position:absolute;width:260px;line-height:14.3px}
.link{color:var(--red);text-decoration:underline}
.bullets{position:absolute;list-style:none;font-weight:700;color:var(--ink);line-height:15px}
.bullets li{padding-left:10px;position:relative}
.bullets li:before{content:"";position:absolute;left:1px;top:4px;border:3px solid transparent;border-left:4px solid var(--red);border-right:0}
.divider{position:absolute;left:133px;top:785px;width:540px;height:8px;background:radial-gradient(ellipse at 50% 0,rgba(0,0,0,.08),transparent 70%)}
.thumb{position:absolute;top:883px;width:94px;height:67px;background:#fff;box-shadow:0 0 3px rgba(0,0,0,.25);padding:3px}
.thumb div{width:100%;height:100%;background:#8aa37a}
.arrow{position:absolute;top:898px;width:32px;height:32px;border-radius:50%;background:var(--red)}
.arrow:after{content:"";position:absolute;top:11px;border:5px solid transparent}
.arrow.prev:after{left:9px;border-right:6px solid #fff;border-left:0}
.arrow.next:after{left:15px;border-left:6px solid #fff;border-right:0}
.carousel-mask{position:absolute;top:880px;width:28px;height:74px;background:#fff}
.contact-box{position:absolute;left:129px;top:982px;width:548px;height:82px;background:#f4f4f4;padding:19px 12px 19px 15px;font-size:16.2px;line-height:20px;color:var(--ink)}
.contact-box em{font-style:normal;color:var(--red)}
.post{position:absolute;left:706px;width:248px;line-height:14.3px}
.post time{display:block;font-size:9px;color:var(--muted);line-height:11px}
.post h3{font-size:12px;font-weight:700;color:var(--ink);line-height:13px}
.post h3.hot{color:var(--red)}
.post .by{font-weight:700;color:var(--ink);margin-top:2px}
.post .by b{color:var(--red)}
.subscribe-input{position:absolute;left:706px;top:968px;width:191px;height:28px;border:1px solid #ccc;background:#fff;box-shadow:inset 0 1px 2px rgba(0,0,0,.1)}
.btn-send{position:absolute;left:903px;top:969px;width:53px;height:27px;background:var(--red);color:#fff;font-size:13px;line-height:27px;text-align:center}
.socials{position:absolute;left:705px;top:1030px;display:flex;gap:4.5px}
.socials i{display:block;width:22px;height:22px;border-radius:2px}
.site-footer{position:absolute;left:0;top:1078px;width:1098px;height:122px;background:var(--footer);color:#fff;text-align:center}
.site-footer:before{content:"";position:absolute;left:110px;top:0;width:840px;height:14px;background:radial-gradient(ellipse at 50% 0,rgba(0,0,0,.35),transparent 70%)}
.site-footer p{position:absolute;left:0;width:1122px;top:65px;font-size:11px}
</style>
</head>
<body>

<header class="site-header">
  <div class="brand"><span class="brand-mark"></span>Harbourline</div>
  <nav class="main-nav">
    <a class="active" style="left:456px">Home</a>
    <a style="left:517px">About us</a>
    <a style="left:601px">Photography</a>
    <a style="left:707px">Property</a>
    <a style="left:790px">Real Estate</a>
    <a style="left:889px">Contact us</a>
  </nav>
</header>

<section class="hero" role="img" aria-label="Portrait photo of the sales consultant on a verandah">
  <div class="hero-panel">
    <h1>Marisska Hartwell</h1>
    <p>Lorem ipsum dolor sit amet, consectetur adipisicing elit, sed do eiusmod tempor incididunt ut labore et dolore magna aliqua. Ut enim ad minim veniam, quis nostrud exercitation ullamco laboris nisi ut aliquip ex ea commodo consequat.</p>
    <span class="btn-readmore">Readmore</span>
    <div class="dots"><i class="on"></i><i></i><i></i><i></i></div>
  </div>
</section>

<h2 class="section-title" style="left:133px;top:410px">Selling</h2>
<div class="rule" style="left:133px;top:440px;width:255px"></div>
<div class="listing-frame" style="left:132px;top:455px">
  <div class="listing-photo" role="img" aria-label="Photo of a house for sale" style="background:#5a7490"></div>
  <svg class="ribbon" width="104" height="76" viewBox="0 0 104 76"><polygon points="18,0 46,0 104,56 104,76" fill="#d41414"/><polygon points="104,56 104,76 100,72" fill="#7a0a0a"/><text x="60" y="34" fill="#fff" font-family="PT Sans,sans-serif" font-size="14" transform="rotate(45 60 30)" text-anchor="middle">Sell</text></svg>
</div>
<h3 class="listing-type" style="left:133px;top:655px">Real Estate Type</h3>
<p class="listing-desc" style="left:133px;top:673px">Lorem ipsum dolor sit amet, consectetur adipisicing elit, sed do eiusmod tempor incididunt ut labore et dolore magna aliqua. <span class="link">Readmore</span></p>
<ul class="bullets" style="left:133px;top:726px"><li>Real Estate Type Small 125</li><li>Real Estate Type Medium 125</li></ul>

<h2 class="section-title" style="left:416px;top:410px">Sold</h2>
<div class="rule" style="left:416px;top:440px;width:256px"></div>
<div class="listing-frame" style="left:415px;top:455px">
  <div class="listing-photo" role="img" aria-label="Photo of a sold house" style="background:#8fae72"></div>
  <svg class="ribbon" width="104" height="76" viewBox="0 0 104 76"><polygon points="18,0 46,0 104,56 104,76" fill="#1662b5"/><polygon points="104,56 104,76 100,72" fill="#0a3566"/><text x="62" y="32" fill="#fff" font-family="PT Sans,sans-serif" font-size="14" transform="rotate(45 62 28)" text-anchor="middle">Sold Out</text></svg>
</div>
<h3 class="listing-type" style="left:416px;top:655px">Real Estate Type</h3>
<p class="listing-desc" style="left:416px;top:673px">Lorem ipsum dolor sit amet, consectetur adipisicing elit, sed do eiusmod tempor incididunt ut labore et dolore magna aliqua. <span class="link">Readmore</span></p>
<ul class="bullets" style="left:416px;top:726px"><li>Real Estate Type Small 125</li><li>Real Estate Type Medium 125</li></ul>

<div class="divider"></div>

<h2 class="section-title" style="left:133px;top:804px">Property</h2>
<p class="listing-desc" style="left:133px;top:829px;width:540px">Lorem ipsum dolor sit amet, consectetur adipisicing elit, sed do eiusmod tempor incididunt ut labore et dolore magna aliqua. <span class="link">Readmore</span></p>
<span class="arrow prev" style="left:141px"></span>
<span class="arrow next" style="left:629px"></span>
<div class="carousel-mask" style="left:158px"></div>
<div class="carousel-mask" style="left:612px"></div>
<div class="thumb" style="left:180px" role="img" aria-label="Property photo"><div></div></div>
<div class="thumb" style="left:295px" role="img" aria-label="Property photo"><div></div></div>
<div class="thumb" style="left:410px" role="img" aria-label="Property photo"><div></div></div>
<div class="thumb" style="left:525px" role="img" aria-label="Property photo"><div></div></div>

<div class="contact-box">if you want to consult about the residential real estate, please contact me at <em>hello@harbourline.com</em> or <em>088-5550142</em></div>

<h2 class="section-title" style="left:708px;top:410px">News</h2>
<div class="rule" style="left:706px;top:440px;width:257px"></div>
<article class="post" style="top:455px"><time>October 10, 2011</time><h3 class="hot">Lorem Ipsum</h3><p>Lorem ipsum dolor sit amet, consectetur adipisicing elit, sed do eiusmod tempor incididunt ut labore et dolore magna aliqua.</p></article>
<article class="post" style="top:537px"><time>October 10, 2011</time><h3>Lorem Ipsum</h3><p>Lorem ipsum dolor sit amet, consectetur adipisicing elit, sed do eiusmod tempor incididunt ut labore et dolore magna aliqua.</p></article>

<h2 class="section-title" style="left:707px;top:633px">Testimonials</h2>
<div class="rule" style="left:706px;top:663px;width:257px"></div>
<article class="post" style="top:677px"><time>October 10, 2011</time><p>Lorem ipsum dolor sit amet, consectetur adipisicing elit, sed do eiusmod tempor.</p><p class="by">Brett Collins - <b>Sidney</b></p></article>
<article class="post" style="top:744px"><time>October 10, 2011</time><p>Lorem ipsum dolor sit amet, consectetur adipisicing elit, sed do eiusmod tempor.</p><p class="by">Liam Hartley - <b>Melbourne</b></p></article>
<article class="post" style="top:810px"><time>October 10, 2011</time><p>Lorem ipsum dolor sit amet, consectetur adipisicing elit, sed do eiusmod tempor.</p><p class="by">Jasmine - <b>Melbourne</b></p></article>

<h2 class="section-title" style="left:707px;top:901px">Subscribde</h2>
<p class="post" style="top:927px">Lorem ipsum dolor sit amet, consectetur adipisicing elit, sed do eiusmod tempor.</p>
<div class="subscribe-input"></div>
<span class="btn-send">Send</span>
<p class="abs" style="left:706px;top:1013px;color:var(--ink)">Follow Us</p>
<div class="socials">
  <i style="background:#3b5998"></i><i style="background:#4fb4e0"></i><i style="background:#1a7bbf"></i><i style="background:#dcdcdc"></i><i style="background:#c8ccd2"></i><i style="background:#f28a1e"></i>
</div>

<footer class="site-footer"><p>Copyright © 2011 harbourline.&nbsp; User Agreement and Privacy Policy.</p></footer>

</body>
</html>
```